LSV AUDITION

I need a post card design (front only) with this on it:
Leap Spin Vibe (this is the main title to be in all caps)
Auditions
Date: Thursday June 30th
6:30-8:30 PM in person
Address: 4170 Wexley BLVD, Oakland CA 94611
video submissions turn in by Sunday July 3rd, 2022 email:LeapSpinVibe22@trovemail.net
Teens and Adults welcomed

SO PLEASE COME UP WITH A DESIGN THATS COLORFUL AND INVITING THX!

```html
<!DOCTYPE html>
<html lang="en">
<head>
<meta charset="UTF-8">
<title>Leap Spin Vibe Auditions Postcard</title>
<link rel="stylesheet" href="https://fonts.googleapis.com/css2?family=Anton&family=Great+Vibes&family=Oswald:wght@600&family=Lato:wght@400;700&family=Pinyon+Script&display=swap">
<style>
  :root {
    --ink-night: #1a0d24;
    --plum-deep: #2c1538;
    --plum-mid: #4a2660;
    --mauve-glow: #8a5a8a;
    --magenta: #e6197f;
    --magenta-dark: #b80f66;
    --violet-tail: #8b3bb0;
    --white: #ffffff;
    --band-black: #0d0b0f;
    --band-grey: #2d2a30;
  }
  * { box-sizing: border-box; margin: 0; padding: 0; }
  html, body { width: 1200px; height: 842px; overflow: hidden; background: #e9e6ec; }
  .postcard {
    position: relative;
    width: 1200px;
    height: 842px;
    overflow: hidden;
    background: var(--ink-night);
  }
  .postcard__backdrop {
    position: absolute; inset: 0;
    background:
      radial-gradient(ellipse at 50% 40%, rgba(138, 90, 138, 0.55), transparent 55%),
      radial-gradient(circle at 92% 70%, rgba(220, 200, 220, 0.35), transparent 22%),
      radial-gradient(circle at 8% 20%, rgba(200, 140, 160, 0.3), transparent 25%),
      linear-gradient(135deg, var(--plum-deep), var(--plum-mid) 50%, var(--plum-deep));
  }
  .postcard__frame {
    position: absolute;
    left: 20px; top: 22px; right: 20px; bottom: 22px;
    border: 2px solid var(--magenta);
    z-index: 3;
    pointer-events: none;
  }
  .postcard__title {
    position: absolute;
    top: 118px; left: 0; width: 100%;
    text-align: center;
    font-family: "Anton", "Oswald", sans-serif;
    font-size: 124px;
    line-height: 1;
    letter-spacing: 3px;
    color: var(--white);
    text-shadow: 4px 4px 0 var(--magenta-dark);
    z-index: 2;
  }
  .postcard__subtitle {
    position: absolute;
    top: 235px; left: 0; width: 100%;
    text-align: center;
    font-family: "Great Vibes", cursive;
    font-size: 132px;
    line-height: 1;
    color: var(--magenta);
    z-index: 2;
  }
  .postcard__ribbon {
    position: absolute;
    top: 400px; left: 138px;
    width: 924px; height: 46px;
    z-index: 2;
  }
  .postcard__ribbon svg { position: absolute; inset: 0; }
  .postcard__ribbon-text {
    position: relative;
    display: block;
    text-align: center;
    font-family: "Oswald", sans-serif;
    font-weight: 600;
    font-size: 30px;
    line-height: 46px;
    letter-spacing: 0.5px;
    color: var(--white);
    padding-right: 20px;
  }
  .postcard__address {
    position: absolute;
    top: 474px; left: 0; width: 100%;
    text-align: center;
    font-family: "Lato", sans-serif;
    font-weight: 700;
    font-size: 31px;
    color: var(--white);
    z-index: 2;
  }
  .postcard__welcome {
    position: absolute;
    top: 548px; left: 0; width: 100%;
    text-align: center;
    font-family: "Pinyon Script", cursive;
    font-size: 46px;
    color: var(--white);
    z-index: 2;
  }
  .postcard__band {
    position: absolute;
    left: 0; bottom: 0;
    width: 1200px; height: 180px;
    z-index: 1;
  }
  .postcard__details {
    position: absolute;
    top: 722px; left: 272px;
    list-style: none;
    font-family: "Lato", sans-serif;
    font-size: 25px;
    color: var(--white);
    z-index: 2;
  }
  .postcard__detail {
    display: flex;
    align-items: center;
    gap: 12px;
    height: 40px;
  }
  .postcard__detail strong { font-weight: 700; }
  .postcard__icon { width: 26px; height: 26px; flex: none; }
</style>
</head>
<body>
<main class="postcard">
  <div class="postcard__backdrop" role="img" aria-label="Dark purple backdrop of layered diamond shapes with glowing bokeh lights and a burst of sparkling particles"></div>

  <svg class="postcard__band" viewBox="0 0 1200 180" aria-hidden="true">
    <defs>
      <linearGradient id="bandShade" x1="0" y1="0" x2="1" y2="0">
        <stop offset="0" stop-color="var(--band-black)"/>
        <stop offset="0.5" stop-color="var(--band-grey)"/>
        <stop offset="1" stop-color="var(--band-black)"/>
      </linearGradient>
    </defs>
    <path d="M0 60 Q600 -10 1200 60 L1200 180 L0 180 Z" fill="url(#bandShade)"/>
    <path d="M0 60 Q600 -10 1200 60" fill="none" stroke="var(--magenta)" stroke-width="9"/>
  </svg>

  <div class="postcard__frame"></div>

  <h1 class="postcard__title">LEAP SPIN VIBE</h1>
  <h2 class="postcard__subtitle">Auditions</h2>

  <div class="postcard__ribbon">
    <svg viewBox="0 0 924 46" preserveAspectRatio="none" aria-hidden="true">
      <polygon points="850,0 924,0 904,23 924,46 850,46" fill="var(--violet-tail)"/>
      <polygon points="0,0 880,0 880,46 0,46 14,23" fill="var(--magenta)"/>
    </svg>
    <span class="postcard__ribbon-text">THURSDAY JUNE 30TH, 6:30-8:30 PM IN PERSON</span>
  </div>

  <p class="postcard__address">4170 Wexley BLVD, Oakland CA 94611</p>
  <p class="postcard__welcome">Teens and Adults Welcomed</p>

  <ul class="postcard__details">
    <li class="postcard__detail">
      <svg class="postcard__icon" viewBox="0 0 26 26" aria-hidden="true">
        <circle cx="13" cy="13" r="13" fill="var(--magenta)"/>
        <rect x="6" y="8" width="10" height="10" rx="1.5" fill="var(--band-black)"/>
        <polygon points="16,11 21,8 21,18 16,15" fill="var(--band-black)"/>
      </svg>
      <span>Video submissions turn in by <strong>Sunday July 3rd, 2022</strong></span>
    </li>
    <li class="postcard__detail">
      <svg class="postcard__icon" viewBox="0 0 26 26" aria-hidden="true">
        <circle cx="13" cy="13" r="13" fill="var(--magenta)"/>
        <rect x="6" y="8" width="14" height="10" rx="1" fill="var(--band-black)"/>
        <polyline points="6.5,8.5 13,14 19.5,8.5" fill="none" stroke="var(--magenta)" stroke-width="1.5"/>
      </svg>
      <span>email: <strong>LeapSpinVibe22@trovemail.net</strong></span>
    </li>
  </ul>
</main>
</body>
</html>
```